36" inch (height) x 96" inch (width) Banner for Baseball Field

Hello. This project is an advertisement that will be printed onto a 3 foot by 8 foot full color banner and placed at little league fields in Southern California. A theme of the banner can be baseball. The company is my law office practicing Estate Planning and Tax Law. I am uploading the current business card, which has the logo, website, and telephone number. You can also pull images from www.rkpembrove.com I would like the banner to be a fun design that incorporates baseball somehow, but draws attention to my law and tax office, and my website. Please be creative, and have fun with it. The colors of my practice are included in the logo. At the bottom, it should say "Attorney Advertisement," but this can be in very small font in the bottom right or left corner.

Target Market(s)

Youth Baseball Fans

Industry/Entity Type

Law; Accounting

Colors

Designer to choose colors to be used in the design.

Requirements
Must have
• My telephone number. My website.
Nice to have
• Would like to see "Estate Planning" and "Tax Law and Preparation" Would also like to see "Attorney" and "CPA" or "Certified Public Accountant" prominently diplayed

```html
<!DOCTYPE html>
<html lang="en">
<head>
<meta charset="utf-8">
<title>RK Pembrove – Ballfield Banner</title>
<link href="https://fonts.googleapis.com/css2?family=PT+Sans:wght@400;700&display=swap" rel="stylesheet">
<style>
  :root {
    --brand-blue: #2a93d0;
    --brand-grey: #9a9a9a;
    --ink: #222222;
    --frame: #2b2b2b;
    --paper: #ffffff;
    --leather-light: #d8975f;
    --leather-dark: #b46c35;
  }
  html, body {
    margin: 0;
    padding: 0;
    width: 1200px;
    height: 433px;
    overflow: hidden;
    background: var(--paper);
    font-family: "PT Sans", Arial, sans-serif;
  }
  .banner {
    position: relative;
    width: 1200px;
    height: 433px;
  }
  .banner-frame {
    position: absolute;
    left: 19px; top: 23px;
    width: 1159px; height: 386px;
    border: 1px solid var(--frame);
    box-sizing: border-box;
  }
  .brand { position: absolute; left: 55px; top: 57px; width: 320px; text-align: center; }
  .brand-mark { display: block; margin: 0 auto; }
  .brand-kicker {
    margin-top: 8px;
    font-size: 16px;
    letter-spacing: 1.5px;
    color: var(--brand-grey);
    line-height: 1;
  }
  .brand-of {
    display: flex; align-items: center; justify-content: center; gap: 6px;
    margin-top: 3px;
    font-size: 9px; color: var(--brand-blue); line-height: 1;
  }
  .brand-of::before, .brand-of::after {
    content: ""; width: 70px; height: 1px; background: var(--brand-blue);
  }
  .brand-name {
    margin-top: 2px;
    font-size: 44px; font-weight: 400;
    letter-spacing: 3px;
    color: var(--brand-blue);
    line-height: 1;
    white-space: nowrap;
  }
  .services {
    position: absolute; left: 63px; top: 242px;
    font-size: 30px; font-weight: 700;
    color: var(--brand-blue);
    line-height: 36px;
    white-space: nowrap;
    letter-spacing: -0.2px;
  }
  .services .sep { color: var(--brand-grey); font-weight: 400; margin: 0 5px; }
  .address {
    position: absolute; left: 63px; top: 330px;
    font-size: 20px; color: var(--brand-blue);
    white-space: nowrap;
  }
  .contact-line {
    position: absolute; left: 63px; top: 362px;
    display: flex; align-items: center; gap: 8px;
    font-size: 21px; color: var(--brand-grey);
    white-space: nowrap;
  }
  .contact-line svg { flex: none; }
  .contact-line .web { margin-left: 10px; }
  .attorney-card {
    position: absolute; right: 62px; top: 44px; text-align: right;
  }
  .attorney-name { font-size: 22px; font-weight: 700; color: var(--brand-blue); line-height: 26px; }
  .attorney-title { font-size: 17px; color: var(--brand-grey); line-height: 20px; }
  .attorney-phone { font-size: 28px; color: var(--brand-grey); line-height: 35px; margin-top: 1px; }
  .attorney-phone + .attorney-phone { margin-top: 0; }
  .hero-art {
    position: absolute; left: 696px; top: 168px;
    width: 412px; height: 192px;
    border-radius: 40px;
    background: linear-gradient(135deg, var(--leather-light), var(--leather-dark));
  }
  .legal-note {
    position: absolute; right: 75px; top: 380px;
    font-size: 9px; color: var(--ink);
  }
</style>
</head>
<body>
<main class="banner">
  <div class="banner-frame"></div>

  <section class="brand">
    <svg class="brand-mark" width="94" height="94" viewBox="0 0 94 94" aria-hidden="true">
      <circle cx="47" cy="47" r="43" fill="none" stroke="var(--brand-blue)" stroke-width="5"/>
    </svg>
    <div class="brand-kicker">THE LAW OFFICES</div>
    <div class="brand-of">OF</div>
    <div class="brand-name">RK PEMBROVE</div>
  </section>

  <div class="services">
    <div>Estate Planning<span class="sep">|</span>Tax Law and Preparation</div>
    <div>Attorney<span class="sep">|</span>CPA<span class="sep">|</span>Certified Public Accountant</div>
  </div>

  <div class="address">228 Harbor Lane, Penthouse Suite 310, Westbrook Hills, California&nbsp; 90000</div>

  <div class="contact-line">
    <svg width="15" height="11" viewBox="0 0 15 11" aria-hidden="true">
      <rect x="0" y="0" width="15" height="11" fill="var(--brand-blue)"/>
      <path d="M0 0 L7.5 6 L15 0 M0 11 L5.5 5 M15 11 L9.5 5" stroke="#fff" stroke-width="1.2" fill="none"/>
    </svg>
    <span>rob@rkpembrove.com</span>
    <svg class="web" width="15" height="15" viewBox="0 0 16 16" aria-hidden="true">
      <g fill="none" stroke="var(--brand-blue)" stroke-width="1.5">
        <circle cx="8" cy="8" r="6.8"/>
        <ellipse cx="8" cy="8" rx="3" ry="6.8"/>
        <path d="M1.2 8 H14.8 M2.4 4.5 H13.6 M2.4 11.5 H13.6"/>
      </g>
    </svg>
    <span>www.rkpembrove.com</span>
  </div>

  <div class="hero-art" role="img" aria-label="Photo of a tan leather baseball glove holding a white baseball, resting on a wooden bat"></div>

  <aside class="attorney-card">
    <div class="attorney-name">Robert K. Pembrove</div>
    <div class="attorney-title">Attorney &amp; CPA</div>
    <div class="attorney-phone">(805) 555-0142</div>
    <div class="attorney-phone">(805) 555-0187</div>
  </aside>

  <div class="legal-note">Attorney Advertisement</div>
</main>
</body>
</html>
```